New Web Design Project

See attachments on the content and concept. Very important that the flow of the tiers stand out

Target Market(s)

Food and Beverage Manufacturing

Industry/Entity Type

Food and Beverage

Coding

Coded - Design and coding required

Number of Pages Required

3 page

Colors
0054AA
0677BA
7BADD7
CADEEF
E8F1F8

```html
<!DOCTYPE html>
<html lang="en">
<head>
<meta charset="utf-8">
<title>Northfield Consulting Group — SQF Consulting</title>
<link href="https://fonts.googleapis.com/css2?family=Playfair+Display:wght@600;700&family=Poppins:wght@400;500;600;700&display=swap" rel="stylesheet">
<style>
:root{
  --blue-deep:#0054AA;
  --blue:#0677BA;
  --blue-soft:#7BADD7;
  --blue-pale:#CADEEF;
  --blue-mist:#E8F1F8;
  --ink:#1b1f29;
  --muted:#4a5160;
  --line:#e3e6ec;
  --white:#ffffff;
  --black:#0b0b0d;
}
*{box-sizing:border-box;margin:0;padding:0}
html,body{width:1200px;height:5080px;overflow:hidden}
body{font-family:"Poppins",sans-serif;color:var(--ink);background:var(--white);position:relative}
.serif{font-family:"Playfair Display",serif}
section,header,footer{position:relative;width:1200px;overflow:hidden}

/* nav */
.site-nav{height:83px;display:flex;align-items:center;padding:0 120px 0 115px;background:var(--white)}
.brand{display:flex;align-items:center;gap:12px;background:#f3f4f6;padding:8px 14px;height:44px}
.brand-dot{width:26px;height:26px;border:2px solid var(--ink);border-radius:50%}
.brand-text{display:flex;flex-direction:column;line-height:1.1}
.brand-name{font-family:"Playfair Display",serif;font-weight:600;font-size:15px}
.brand-tag{font-size:9px;letter-spacing:.8px;color:var(--muted)}
.nav-links{display:flex;gap:46px;margin-left:auto;font-size:14px;color:var(--ink)}
.nav-mode{width:18px;height:18px;margin-left:36px}
.btn{display:inline-flex;align-items:center;justify-content:center;border-radius:22px;font-weight:600;font-size:14px;height:38px;padding:0 20px}
.btn-blue{background:var(--blue-deep);color:var(--white)}
.btn-white{background:var(--white);color:var(--blue-deep)}
.site-nav .btn{margin-left:30px;height:38px;padding:0 18px}

/* hero */
.hero{height:597px}
.hero-photo{position:absolute;inset:0;background:linear-gradient(180deg,#6d7781 0%,#4f5963 55%,#3e4852 100%)}
.hero-shade{position:absolute;inset:0;background:rgba(20,30,45,.35)}
.hero-copy{position:absolute;top:100px;left:0;width:1200px;text-align:center;color:var(--white)}
.hero-copy h1{font-family:"Playfair Display",serif;font-weight:700;font-size:54px;line-height:56px}
.hero-copy p{margin:38px auto 0;width:640px;font-size:15px;line-height:20px}
.hero-actions{margin-top:26px;display:flex;gap:20px;justify-content:center}
.hero-wave{position:absolute;left:0;bottom:0;width:1200px;height:150px}

/* stats */
.stats{height:180px}
.stat{position:absolute;top:62px;width:240px;margin-left:-120px;text-align:center}
.stat b{display:block;font-size:38px;font-weight:700;line-height:44px}
.stat span{font-size:14px;color:var(--ink)}
.stats-rule{position:absolute;left:120px;right:120px;bottom:18px;border-top:1px solid var(--line)}

/* headings */
.kicker{font-weight:700;font-size:19px;letter-spacing:.5px;color:var(--blue-deep);text-align:center}
.section-title{font-family:"Playfair Display",serif;font-weight:700;font-size:31px;text-align:center;margin-top:12px}
.section-lead{font-size:14px;line-height:23px;text-align:center;color:var(--muted);margin:14px auto 0}

/* services */
.services{height:1065px;padding-top:68px}
.card-grid{position:absolute;top:245px;left:120px;display:grid;grid-template-columns:repeat(3,300px);grid-auto-rows:345px;gap:25px 28px}
.card{background:var(--white);border-radius:6px;box-shadow:0 4px 18px rgba(10,30,60,.12);padding:40px 22px 0;text-align:center}
.card svg{width:70px;height:70px;stroke:var(--blue-deep);fill:none;stroke-width:2.4;stroke-linecap:round;stroke-linejoin:round}
.card h3{font-size:18px;font-weight:600;margin-top:32px}
.card p{font-size:13px;line-height:19px;color:var(--muted);margin-top:16px}
.card-featured{background:linear-gradient(180deg,var(--blue) 0%,var(--blue-deep) 100%);color:var(--white);border:2px solid var(--blue-deep)}
.card-featured svg{stroke:var(--white)}
.card-featured p{color:var(--white)}

/* why */
.why{height:932px;background:linear-gradient(180deg,var(--blue) 0%,var(--blue-deep) 100%);color:var(--white);padding-top:66px}
.why .kicker{color:var(--white)}
.why .section-lead{color:var(--white);width:720px}
.why-photo{position:absolute;left:0;top:270px;width:549px;height:595px;background:linear-gradient(135deg,#c9d2dc 0%,#9eacbb 45%,#5d7088 100%)}
.benefits{position:absolute;left:574px;top:285px;width:510px;list-style:none}
.benefit{display:flex;gap:22px;margin-bottom:32px}
.benefit svg{flex:0 0 34px;width:34px;height:34px;stroke:var(--white);fill:none;stroke-width:2.4;stroke-linecap:round;stroke-linejoin:round}
.benefit h4{font-size:17px;font-weight:600}
.benefit p{font-size:13px;line-height:21px;color:var(--blue-pale);margin-top:6px}

/* process */
.process{height:767px;padding-top:82px}
.process-track{position:absolute;top:0;left:0;width:1200px;height:767px}
.step-icon{stroke:var(--white);fill:none;stroke-width:3;stroke-linecap:round;stroke-linejoin:round}
.step-text{position:absolute;width:270px;margin-left:-135px;text-align:center}
.step-text h4{font-size:18px;font-weight:600}
.step-text p{font-size:13px;line-height:19px;color:var(--muted);margin-top:8px}

/* testimonial */
.testimonial{height:379px;background:var(--blue)}
.testimonial-photo{position:absolute;inset:0;background:linear-gradient(90deg,#8fb4d6 0%,#4f8fc4 30%,var(--blue) 55%,var(--blue) 100%)}
.quote{position:absolute;left:440px;top:110px;width:650px;text-align:center;color:var(--white)}
.quote blockquote{font-family:"Playfair Display",serif;font-weight:600;font-size:29px;line-height:34px}
.quote cite{display:block;font-style:normal;font-weight:600;font-size:17px;margin-top:20px}

/* credentials */
.credentials{height:369px}
.cred{position:absolute;top:89px;width:218px;height:191px;background:var(--white);box-shadow:0 4px 18px rgba(10,30,60,.12);border-radius:4px;display:flex;flex-direction:column;align-items:center;justify-content:center;text-align:center}
.cred svg{width:68px;height:68px;stroke:var(--blue-deep);fill:none;stroke-width:2.2;stroke-linecap:round;stroke-linejoin:round}
.cred span{font-size:18px;font-weight:600;line-height:22px;margin-top:14px}
.cred-active{border:3px solid var(--blue-deep)}

/* cta */
.cta{height:342px;background:var(--white)}
.cta-photo{position:absolute;inset:0;background:linear-gradient(90deg,#9aa6b3 0%,#c3ccd5 25%,#edf0f3 45%,#ffffff 60%)}
.cta-copy{position:absolute;left:480px;top:85px;width:620px;text-align:center}
.cta-copy h2{font-family:"Playfair Display",serif;font-weight:700;font-size:38px}
.cta-copy p{font-size:15px;line-height:22px;margin-top:14px}
.cta-actions{display:flex;gap:12px;justify-content:center;margin-top:26px}
.cta-actions .btn{height:42px;font-size:15px;padding:0 24px}

/* footer */
.site-footer{height:366px;background:var(--black);color:var(--white)}
.foot-mark{position:absolute;left:122px;top:66px;width:104px;height:104px;border:4px solid #8b8d92;border-radius:50%}
.foot-col{position:absolute;top:70px}
.foot-col h5{font-size:18px;font-weight:500;margin-bottom:22px}
.foot-col p,.foot-col li{font-size:12px;line-height:18px;color:#cfd1d6;list-style:none}
.foot-col li{margin-bottom:8px}
.foot-rule{position:absolute;left:120px;right:120px;top:290px;border-top:1px solid #33353a}
.copyright{position:absolute;top:318px;width:1200px;text-align:center;font-size:12px}
</style>
</head>
<body>

<header class="site-nav">
  <div class="brand">
    <span class="brand-dot"></span>
    <div class="brand-text">
      <span class="brand-name">Northfield Consulting Group</span>
      <span class="brand-tag">FOOD SAFETY &amp; SQF CERTIFICATION</span>
    </div>
  </div>
  <nav class="nav-links"><span>Services</span><span>Benefits</span><span>Process</span><span>Contact</span></nav>
  <svg class="nav-mode" viewBox="0 0 24 24" fill="none" stroke="#1b1f29" stroke-width="2"><path d="M20 14.5A8 8 0 1 1 9.5 4a6.5 6.5 0 0 0 10.5 10.5z"/></svg>
  <span class="btn btn-blue">Get SQF Consultation</span>
</header>

<section class="hero">
  <div class="hero-photo" role="img" aria-label="Food production plant with workers in hairnets and lab coats at stainless steel lines"></div>
  <div class="hero-shade"></div>
  <div class="hero-copy">
    <h1>Hire a tech-driven SQF Team<br>that carries you across the<br>certification finish line.</h1>
    <p>At Northfield Consulting Group, we focus exclusively on SQF — combining real plant experience with smart technology so your team can stay focused on production while we handle the path to certification and beyond.</p>
    <div class="hero-actions"><span class="btn btn-blue">Get SQF Consultation</span><span class="btn btn-white">Explore Services</span></div>
  </div>
  <svg class="hero-wave" viewBox="0 0 1200 150" preserveAspectRatio="none">
    <path d="M0 60 Q600 170 1200 60 L1200 150 L0 150 Z" fill="var(--blue-deep)"/>
    <path d="M0 80 Q600 180 1200 80 L1200 150 L0 150 Z" fill="var(--blue)"/>
    <path d="M0 100 Q600 190 1200 100 L1200 150 L0 150 Z" fill="#ffffff"/>
  </svg>
</section>

<section class="stats">
  <div class="stat" style="left:237px"><b>15+</b><span>Clients Onboarded</span></div>
  <div class="stat" style="left:452px"><b>100%</b><span>SQF Focused</span></div>
  <div class="stat" style="left:683px"><b>Digital</b><span>Platform Built Programs</span></div>
  <div class="stat" style="left:950px"><b>US</b><span>Nationwide Coverage</span></div>
  <div class="stats-rule"></div>
</section>

<section class="services" id="services">
  <p class="kicker">WHAT WE DO</p>
  <h2 class="section-title">SQF Consulting, Implementation &amp; Onboarding</h2>
  <p class="section-lead" style="width:760px">We help food and beverage manufacturers achieve and maintain SQF certification with confidence, using practical programs and digital tools that work on the floor — not just on audit day.</p>
  <div class="card-grid">
    <article class="card card-featured">
      <svg viewBox="0 0 48 48"><path d="M12 4h17l9 9v31H12z"/><path d="M29 4v9h9"/><path d="M19 22h13M19 28h13M19 34h13"/><circle cx="16" cy="22" r=".6"/><circle cx="16" cy="28" r=".6"/><circle cx="16" cy="34" r=".6"/></svg>
      <h3>SQF Program Design</h3>
      <p>We design your complete SQF system from scratch — HACCP/food safety plans, prerequisite programs, SOPs, forms, logs, and all required documentation tailored to your facility.</p>
    </article>
    <article class="card">
      <svg viewBox="0 0 48 48"><rect x="8" y="9" width="32" height="22" rx="2"/><path d="M4 37h40"/></svg>
      <h3>Digital Platform Build</h3>
      <p>We build your SQF program directly into modern food safety software like PlantLog.app or SafeLine.app — digitizing forms, checklists, monitoring logs, and workflows so your team runs paperless.</p>
    </article>
    <article class="card">
      <svg viewBox="0 0 48 48"><path d="M9 26v-4a15 15 0 0 1 30 0v4"/><rect x="5" y="24" width="7" height="11" rx="3"/><rect x="36" y="24" width="7" height="11" rx="3"/><path d="M39 35c0 5-5 7-11 7"/><rect x="16" y="14" width="16" height="12" rx="3"/><path d="M20 20h.1M24 20h.1M28 20h.1"/></svg>
      <h3>Coaching &amp; Support</h3>
      <p>After building your system, we coach your team to own and maintain it day-to-day. You run the program; we provide ongoing expert guidance so you stay audit-ready at all times.</p>
    </article>
    <article class="card">
      <svg viewBox="0 0 48 48"><path d="M12 6h24v36H12z"/><path d="M17 12h14M17 17h14M17 22h8"/><circle cx="27" cy="32" r="7"/><path d="M24 32l2 2 4-4"/></svg>
      <h3>Gap Assessments</h3>
      <p>We evaluate where your facility stands against SQF requirements, identify gaps, and provide a clear roadmap to close them before your audit — no surprises on certification day.</p>
    </article>
    <article class="card">
      <svg viewBox="0 0 48 48"><circle cx="24" cy="13" r="5"/><circle cx="12" cy="18" r="4"/><circle cx="36" cy="18" r="4"/><path d="M17 40V28a7 7 0 0 1 14 0v12z"/><path d="M6 40V31a6 6 0 0 1 9-5M42 40V31a6 6 0 0 0-9-5M6 40h36"/></svg>
      <h3>Bilingual Team Support</h3>
      <p>Our team in Central America supports Spanish-speaking employees within your operation — delivering training, documentation, and coaching in the language your floor team actually speaks.</p>
    </article>
    <article class="card">
      <svg viewBox="0 0 48 48"><path d="M24 4l16 6v12c0 11-7 18-16 22C15 40 8 33 8 22V10z"/><path d="M24 16v14"/></svg>
      <h3>Sanitation &amp; Regulatory</h3>
      <p>From sanitation program design to environmental monitoring, we help you build internal capabilities that meet USDA, FDA, and FSMA requirements and reduce dependence on external contractors.</p>
    </article>
  </div>
</section>

<section class="why" id="benefits">
  <p class="kicker">WHY NORTHFIELD CONSULTING</p>
  <h2 class="section-title">Built for Small &amp; Mid-Size Manufacturers</h2>
  <p class="section-lead">You don't need to hire a full-time food safety director or figure out SQF alone. We bring the expertise and technology — you stay focused on production. Consultant reviewing digital food safety compliance system in a manufacturing facility.</p>
  <div class="why-photo" role="img" aria-label="Consultant holding a tablet showing a food safety compliance checklist"></div>
  <ul class="benefits">
    <li class="benefit"><svg viewBox="0 0 34 34"><circle cx="17" cy="17" r="14"/><path d="M11 17l5 5 12-13"/></svg><div><h4>Lower Cost Than a Full-Time Hire</h4><p>Get a complete SQF team — program design, digital implementation, and coaching — at a fraction of the cost of hiring a full-time SQF Practitioner.</p></div></li>
    <li class="benefit"><svg viewBox="0 0 34 34"><circle cx="17" cy="17" r="14"/><path d="M11 17l5 5 12-13"/></svg><div><h4>Your Program Lives in Software</h4><p>No more binders and spreadsheets. Your SQF system is built into PlantLog.app or SafeLine.app — organized, accessible, and always audit-ready.</p></div></li>
    <li class="benefit"><svg viewBox="0 0 34 34"><circle cx="17" cy="17" r="14"/><path d="M11 17l5 5 12-13"/></svg><div><h4>You Own It, We Support It</h4><p>We build the system and train your team. You maintain and run it day-to-day. We stay on call with coaching and advisory so you never feel stuck.</p></div></li>
    <li class="benefit"><svg viewBox="0 0 34 34"><circle cx="17" cy="17" r="14"/><path d="M11 17l5 5 12-13"/></svg><div><h4>Flexible, Low-Risk Engagement</h4><p>Start with a 3-month commitment, then go month-to-month. Cancel anytime with 30 days notice. We earn your business every month.</p></div></li>
    <li class="benefit"><svg viewBox="0 0 34 34"><circle cx="17" cy="17" r="14"/><path d="M11 17l5 5 12-13"/></svg><div><h4>Bilingual Floor-Level Support</h4><p>With our Central America team, we provide training and documentation in Spanish so every member of your production team understands and follows the program.</p></div></li>
  </ul>
</section>

<section class="process" id="process">
  <p class="kicker">HOW IT WORKS</p>
  <h2 class="section-title">From Discovery to Certification</h2>
  <p class="section-lead">A clear, structured path that takes the guesswork out of SQF.</p>
  <svg class="process-track" viewBox="0 0 1200 767">
    <defs>
      <linearGradient id="stepFill" x1="0" y1="0" x2="0" y2="1"><stop offset="0" stop-color="#0677BA"/><stop offset="1" stop-color="#0054AA"/></linearGradient>
    </defs>
    <g fill="none" stroke="#d9dde3" stroke-width="3">
      <path d="M122 473 A120 120 0 0 0 361 473"/>
      <path d="M361 473 A120 120 0 0 1 602 473"/>
      <path d="M602 473 A120 120 0 0 0 839 473"/>
      <path d="M839 473 A120 120 0 0 1 1080 473"/>
      <path d="M122 473 V430 M1080 473 V516"/>
    </g>
    <g fill="#7BADD7">
      <circle cx="122" cy="473" r="8"/><circle cx="361" cy="473" r="8"/><circle cx="602" cy="473" r="8"/><circle cx="839" cy="473" r="8"/><circle cx="1080" cy="473" r="8"/>
    </g>
    <g fill="url(#stepFill)">
      <circle cx="241" cy="473" r="76"/><circle cx="481" cy="473" r="76"/><circle cx="720" cy="473" r="76"/><circle cx="960" cy="473" r="76"/>
    </g>
    <g class="step-icon">
      <path d="M224 448c-6 4-8 12-3 22 6 12 16 22 28 27 9 4 16 1 20-4l-9-9-7 4c-6-3-12-9-15-15l4-7z"/>
      <path d="M248 446a22 22 0 0 1 20 20M248 436a32 32 0 0 1 30 30"/>
      <path d="M464 443h24l10 10v46h-34z"/><path d="M472 463h18M472 473h18M472 483h18"/>
      <circle cx="720" cy="473" r="34"/><circle cx="708" cy="464" r="2"/><circle cx="732" cy="464" r="2"/><path d="M706 482q14 12 28 0"/>
      <rect x="936" y="452" width="48" height="32" rx="3"/><path d="M928 494h64"/>
    </g>
  </svg>
  <div class="step-text" style="left:241px;top:268px"><h4>Discovery Call</h4><p>We learn about your facility, your current systems, and where you are in the SQF journey. No pressure — just a conversation.</p></div>
  <div class="step-text" style="left:720px;top:268px"><h4>Build &amp; Implement</h4><p>We design your SQF program and build it directly into your digital food safety platform — forms, logs, SOPs, HACCP plans, all of it.</p></div>
  <div class="step-text" style="left:481px;top:570px"><h4>Gap Assessment</h4><p>We evaluate your facility against SQF requirements, identify what's missing, and give you a clear roadmap with priorities.</p></div>
  <div class="step-text" style="left:960px;top:577px"><h4>Coach &amp; Certify</h4><p>We train your team, run mock audits, and prepare you for certification day. Then we stay on as your ongoing SQF advisory partner.</p></div>
</section>

<section class="testimonial">
  <div class="testimonial-photo" role="img" aria-label="Production workers in hairnets reviewing a tablet on the plant floor"></div>
  <div class="quote">
    <blockquote>"Northfield Consulting Group didn't just hand us a binder. They built our entire SQF system into software and coached our team until we owned it. We passed our first audit with confidence."</blockquote>
    <cite>— SQF-Certified Manufacturing Client</cite>
  </div>
</section>

<section class="credentials">
  <div class="cred cred-active" style="left:120px"><svg viewBox="0 0 48 48"><circle cx="24" cy="16" r="9"/><path d="M8 42c0-9 7-14 16-14s16 5 16 14z"/></svg><span>SQF Practitioner</span></div>
  <div class="cred" style="left:369px"><svg viewBox="0 0 48 48"><circle cx="24" cy="24" r="19"/><circle cx="18" cy="20" r="1.5"/><circle cx="30" cy="20" r="1.5"/><path d="M16 29q8 8 16 0"/></svg><span>Six Sigma<br>Black Belt</span></div>
  <div class="cred" style="left:616px"><svg viewBox="0 0 48 48"><path d="M9 26v-4a15 15 0 0 1 30 0v4"/><rect x="5" y="24" width="7" height="11" rx="3"/><rect x="36" y="24" width="7" height="11" rx="3"/><path d="M39 35c0 5-5 7-11 7"/><rect x="16" y="14" width="16" height="12" rx="3"/></svg><span>Remote &amp;<br>On-Site</span></div>
  <div class="cred" style="left:863px"><svg viewBox="0 0 48 48"><circle cx="20" cy="12" r="6"/><path d="M8 34c0-7 5-11 12-11"/><rect x="24" y="22" width="18" height="12" rx="1"/><path d="M6 40h38"/><circle cx="33" cy="28" r="2"/></svg><span>Digital-First</span></div>
</section>

<section class="cta" id="contact">
  <div class="cta-photo" role="img" aria-label="Quality specialists in hairnets and lab coats reviewing data on a tablet"></div>
  <div class="cta-copy">
    <h2>Ready to Talk SQF?</h2>
    <p>Share a few details about your facility and where you are in the SQF journey. We'll follow up with a brief discovery call and a clear next step.</p>
    <div class="cta-actions"><span class="btn btn-blue">Get My SQF Consultation</span><span class="btn btn-blue">Visit plantqualityhub.com</span></div>
  </div>
</section>

<footer class="site-footer">
  <div class="foot-mark"></div>
  <div class="foot-col" style="left:280px;width:290px">
    <h5>Northfield Consulting Group LLC</h5>
    <p>Tech-driven SQF consulting for small and mid-size US food manufacturers. Based in Modesto, CA — serving clients across North America.</p>
  </div>
  <div class="foot-col" style="left:641px">
    <h5>Services</h5>
    <ul><li>SQF Program Design</li><li>Digital Platform Build</li><li>Coaching &amp; Support</li><li>Gap Assessments</li><li>Sanitation Programs</li></ul>
  </div>
  <div class="foot-col" style="left:886px">
    <h5>Connect</h5>
    <ul><li>Email Us</li><li>plantqualityhub.com</li><li>Social Profile</li></ul>
  </div>
  <div class="foot-rule"></div>
  <p class="copyright">© 2026 Northfield Consulting Group LLC. All rights reserved.</p>
</footer>

</body>
</html>
```